Greek Souvlaki Restaurant Menu Design

We would like to redesign our menu (at the moment just a price-list without any graphics) and create something more fun.

You can find all the items we are offering at the following link / our e-shop:
https://olivebranchkitchen.example/orders/en/order/
I have also attached a printout of the above with hand written notes on the sections and items that will be included.

Our menu is divided to a couple of parts:
- Souvlaki Bar and Grill
- Authentic Greek Cuisine
- Wine List
- Desserts
- Bakaliko

This project will take on the first part of our menu, which is the Souvlaki Bar and Grill. If we are happy with your design, we will then develop the rest of our menu.

Souvlaki Bar and Grill
---------------------------

Our souvlaki can be customised to the customer requirements. The following links have similar set ups:

WOW!Patty
https://gr.pinboardly.example/pin/100000000000000001/
I like the way they have set it up, but the graphics and colours used are not my thing. I also like they way they have split up the steps, choose, top it of, etc.

The Krokk
https://gr.pinboardly.example/pin/100000000000000002/
I hate the step 1,2,3 on the left side. It does not make it playful. Like the fact that they have used pictures of the ingredients.

https://gr.pinboardly.example/pin/100000000000000003/
Hate the graphics, like the concept.

-------------

First Sections: Our Souvliaki Pita Wrap

The steps to customise a souvlaki can be found on the following link:
https://olivebranchkitchen.example/orders/en/order/ and choose pita wrap.

Most of the one side of our Souvliaki/Grill menu should be dedicated to our Pita Wraps.

It should have a small description of the Greek Souvlaki Pita Wrap. Something along the lines of "Get a whole meal all wrapped up with our delicious Greek Pita Wraps. Containing protein, sauce and salad". Improvements of this line are welcome.

It should then have the steps to customise it.

Step One.
Choose Base:
1. Chicken Skewer
2. Pork Skewer
3. etc
Price and options can be found on the above link on our website

Step Two.
Add one of our delicious home made sauces.
Options can be found on our website.

Step Three
Finalise it with the ingredients of your choice.
The customer can select multiple incredients

Step Four.
Feeling Hungry? Add extras:
Extras and Prices can be found on the link provided.

Buy two wraps and save. Takeaway only!
You will find this option as "Double Souvlaki Pita Wrap Offer."
Instead of 2x5.5 = £11 pay £10.5. This offer should also be mentioned somewhere on this section.

-----

Second Section - Our Platters

Skewers Platter and Gyros Platter

Options can be found by clicking on the items on the link provided.

Extras and Pita Bread option are common. Meat options are different and skewers have a choice of side. Meat options have 2/3 skewers and 200/300 grams of gyros, so they can probably be combined somehow.

These section can also be called Naked / Open Souvlaki Platters

Third Section
From Our Grill

All options from this section together with modifiers (can be see if you click on each item). I would like pictures from each item.

Forth Section
Meal Deals, starter combo and Set Menu.

Meal Deal for 1/2 and 4 are wraps with extras. The for 4 is not on the pdf and will be up on our website soon, so please check. I think those are easy to e incorporated next to the pita wrap section as upgrades to save.

Set menus are various items.

If they can fit on this page somehow we incorporate them, if not we can make a separate page with the offers / meals deals. If a separate page is created them the meal deal from our kitchen and vegetarean set menu should also be included.

Fifth Section
Salads and Starter

I would like all options from Hot and Cold starter and our salad. I would like pictures next to all options, if possible.

-----

Final notes/ideas.

Wraps, platters and grill could be one page front and back. Salads and starters could be a different page(s) or sections.

The menu should be easily updated and we would like a format where we can update prices and descriptions.

Prices and descriptions can be found on the link provided.

Feel free to improve our descriptions and titles. Please do mention where you made improvements, so we can approve them.

Our kitchen, dessert and wine menu will be given as a separate project and priority will be given to the person that won this competition.

If you need better quality pictures please let us know, most of the pictures we do have them in raw format too.

------

Some designs that I like. To give you an idea of the design I would like to see:

https://www.craftmarketly.example/listing/100000001/american-menu-restaurant-cafe-menus
I would love to see something like that for the grill/salad/starter side of our menu, since it has space for pictures.

https://gr.pinboardly.example/pin/100000000000000004/
I would love to see something like that, where the incredients of a souvlaki come together. This is optional and does not have to be there.

https://gr.pinboardly.example/pin/100000000000000005/

https://gr.pinboardly.example/pin/100000000000000006/

https://gr.pinboardly.example/pin/100000000000000007/

https://gr.pinboardly.example/pin/100000000000000008/

Target Market(s)

London

Font styles to use
Serif
Sans Serif

Colors
abd037
3277b5
33a6d7

Requirements
Must have
• Build your own souvlaki section. See description for examples.

Pictures for starters and salads.

Should be elegant
Nice to have
• Incorporate our relevant meal deals on the souvlaki pita section

```html
<!DOCTYPE html>
<html lang="en">
<head>
<meta charset="utf-8">
<title>Olive Branch Kitchen – Souvlaki Pita Wraps & Platters</title>
<link href="https://fonts.googleapis.com/css2?family=Kaushan+Script&family=Open+Sans:ital,wght@0,400;0,600;0,700;1,400&display=swap" rel="stylesheet">
<style>
  :root{
    --board:#13223a;
    --board-light:#1c3150;
    --green:#abd037;
    --blue:#3277b5;
    --sky:#33a6d7;
    --cream:#f5f2e6;
    --yellow:#e7d84b;
    --ink:#13223a;
  }
  *{margin:0;padding:0;box-sizing:border-box}
  html,body{width:849px;height:1200px;overflow:hidden;background:var(--board)}
  .menu{position:relative;width:849px;height:1200px;overflow:hidden;
    background:radial-gradient(ellipse at 40% 35%,var(--board-light),var(--board) 70%);
    font-family:"Open Sans",Arial,sans-serif;color:var(--cream)}
  .abs{position:absolute}
  .script{font-family:"Kaushan Script","Brush Script MT",cursive;font-weight:400}

  .menu-title{left:28px;top:12px;font-size:38px;color:var(--green);line-height:1.1}
  .title-pill{left:505px;top:18px;width:240px;height:40px;border-radius:20px;background:var(--cream);
    color:var(--ink);font-size:24px;display:flex;align-items:center;justify-content:center}
  .intro{left:28px;top:60px;width:430px;font-size:10.5px;line-height:1.4;color:var(--cream)}

  .photo{background:linear-gradient(135deg,#c99b5a,#8a5a2c 55%,#d9c7a0)}
  .photo-wrap{left:480px;top:70px;width:369px;height:280px;border-radius:140px 0 0 140px;
    background:radial-gradient(circle at 45% 45%,#e0b36d,#a66a2f 55%,#f1ead6 80%)}

  .step{display:flex;align-items:center;gap:8px;height:32px}
  .step-num{width:28px;height:28px;border-radius:50%;background:var(--green);color:var(--ink);
    font-family:"Kaushan Script",cursive;font-size:18px;display:flex;align-items:center;justify-content:center;flex:none}
  .step-title{font-size:22px;color:var(--green);white-space:nowrap}
  .step-note{font-size:17px;color:var(--green);white-space:nowrap}

  .options{list-style:none;font-size:12px;line-height:16px;margin:6px 0 0 22px}
  .options li{display:flex;white-space:nowrap}
  .options li::before{content:"";width:5px;height:5px;border-radius:50%;background:var(--cream);margin:6px 12px 0 0;flex:none}
  .options .name{width:175px}
  .options.wide .name{width:160px}

  .price-badge{left:338px;top:158px;width:80px;height:80px;border-radius:50%;background:var(--green);
    color:var(--ink);font-weight:700;font-size:20px;display:flex;align-items:center;justify-content:center;
    border:3px solid var(--cream)}
  .offer{left:490px;top:356px;width:320px;font-size:12px;line-height:1.35;color:var(--yellow);font-style:italic;text-align:center}
  .offer strong{font-style:normal}

  .platters-band{left:0;top:540px;width:849px;height:66px;display:flex;align-items:center;justify-content:center;gap:24px}
  .band-line{width:140px;height:2px;background:var(--green)}
  .platters-title{font-size:44px;color:var(--cream);white-space:nowrap}
  .photo-gyros{left:0;top:608px;width:215px;height:118px;border-radius:0 60px 60px 0;
    background:linear-gradient(120deg,#f0ede2,#c9833f 45%,#6f9a3a)}
  .photo-skewers{left:637px;top:608px;width:212px;height:118px;border-radius:60px 0 0 60px;
    background:linear-gradient(240deg,#f0ede2,#b7763a 45%,#e5c24a)}
  .pill{height:30px;border-radius:15px;display:flex;align-items:center;justify-content:center;font-weight:700;font-size:15px}
  .pill-price{background:var(--green);color:var(--ink)}
  .pill-name{background:var(--green);color:var(--ink);font-family:"Kaushan Script",cursive;font-weight:400;font-size:19px;border-radius:4px}

  .platter-desc{width:385px;font-size:10.5px;line-height:1.45;color:var(--yellow);font-style:italic}
  .sub-head{font-size:21px;color:var(--green);line-height:1.2;white-space:nowrap}
  .plain{list-style:none;font-size:12.5px;line-height:17px}
  .plain li{display:flex;white-space:nowrap}
  .plain .name{flex:1}

  .brand{left:28px;top:1060px;display:flex;align-items:center;gap:10px;font-size:20px;color:var(--cream);line-height:1.1}
  .brand-dot{width:14px;height:14px;border-radius:50%;background:var(--green)}
</style>
</head>
<body>
<main class="menu">

  <h1 class="abs script menu-title">Our Souvlaki Pita Wrap</h1>
  <div class="abs script title-pill">Make it Your Own</div>
  <p class="abs intro">Get a whole meal all wrapped up with our Greek pita wraps. Choose the base (meat, gyros, halloumi or kebab), add one of our home made sauces and fill it up with the fresh ingredients of your choice. If you are feeling extra hungry, add an extra skewer or double up your pita.</p>

  <div class="abs photo photo-wrap" role="img" aria-label="Photo of a souvlaki pita wrap with fries in branded paper"></div>

  <section class="abs" style="left:28px;top:114px">
    <div class="step"><span class="step-num">1</span><span class="script step-title">Choose Your Base</span><span class="script step-note">(Choose 1)</span></div>
    <ul class="options">
      <li><span class="name">Chicken</span><span>£ .50</span></li>
      <li><span class="name">Pork</span><span>£ .50</span></li>
      <li><span class="name">Gyros Chicken</span><span>£1.50</span></li>
      <li><span class="name">Gyros Pork</span><span>£1.50</span></li>
      <li><span class="name">Mixed Gyros (Chicken &amp; Pork)</span><span>£2.00</span></li>
      <li><span class="name">Kebab</span><span>£2.50</span></li>
      <li><span class="name">Sausage</span><span>£ .50</span></li>
      <li><span class="name">Halloumi</span><span>£ .50</span></li>
      <li><span class="name">No Base</span><span>(V) £ .50</span></li>
    </ul>
  </section>

  <div class="abs price-badge">£ 5.50</div>

  <section class="abs" style="left:28px;top:302px">
    <div class="step"><span class="step-num">2</span><span class="script step-title">Get Sauced</span><span class="script step-note">(Choose 1)</span></div>
    <ul class="options">
      <li><span class="name">Tzatziki</span><span>(V)</span></li>
      <li><span class="name">Tyrokafteri</span><span>(V)</span></li>
      <li><span class="name">Burger Sauce</span><span>(V)</span></li>
      <li><span class="name">No Sauce</span></li>
    </ul>
  </section>

  <section class="abs" style="left:28px;top:412px">
    <div class="step"><span class="step-num">3</span><span class="script step-title">Fill it Up!</span><span class="script step-note">(Choose any)</span></div>
    <ul class="options">
      <li><span class="name">Fries</span></li>
      <li><span class="name">Tomatoes</span></li>
      <li><span class="name">Onions</span></li>
      <li><span class="name">No Ingredient</span></li>
    </ul>
  </section>

  <p class="abs offer">Buy two wraps and save! Takeaway only!<br><strong>"Double Souvlaki Pita Wrap Offer"</strong><br>Instead of 2x5.5 = £11 pay £10.5</p>

  <section class="abs" style="left:440px;top:412px">
    <div class="step"><span class="step-num">4</span><span class="script step-title">Feelin' Extra Hungry?</span><span class="script step-note">(Add Extras)</span></div>
    <ul class="options wide">
      <li><span class="name">Double Pita Bread</span><span>£ 1.00</span></li>
      <li><span class="name">Add Pork Skewer</span><span>£ 2.50</span></li>
      <li><span class="name">Add Chicken Skewer</span><span>£ 2.50</span></li>
      <li><span class="name">Add Kebab (lamb+beef)</span><span>£ 2.50</span></li>
      <li><span class="name">Add Sausage</span><span>£ 2.50</span></li>
    </ul>
  </section>

  <div class="abs platters-band">
    <span class="band-line"></span>
    <h2 class="script platters-title">Open Souvlaki Platters</h2>
    <span class="band-line"></span>
  </div>

  <div class="abs photo photo-gyros" role="img" aria-label="Photo of a gyros platter with fries, salad and pita"></div>
  <div class="abs photo photo-skewers" role="img" aria-label="Photo of a skewers platter with fries and pita"></div>

  <div class="abs pill pill-price" style="left:113px;top:713px;width:86px">£ 13.00</div>
  <div class="abs pill pill-name" style="left:240px;top:713px;width:142px">Gyros Platter</div>
  <div class="abs pill pill-name" style="left:425px;top:713px;width:150px">Skewers Platter</div>
  <div class="abs pill pill-price" style="left:650px;top:713px;width:86px">£ 10.00</div>

  <section class="abs" style="left:28px;top:752px;width:390px">
    <p class="platter-desc">Traditional Greek Gyro Plate or Chicken Gyros. Generous portion served with refreshing tomato sauce, pita bread, fries, onion, tomatoes and tzatziki. A great selection of vegetable sides to make it a delicious complete meal.</p>
    <div style="display:flex;gap:28px;margin-top:14px">
      <div style="width:250px">
        <h3 class="script sub-head">Meat Options <span style="font-size:16px">(200G)</span></h3>
        <ul class="plain">
          <li><span class="name">Chicken Gyros</span></li>
          <li><span class="name">Pork Gyros</span></li>
          <li><span class="name">Mixed Gyros (Chicken &amp; Pork)</span><span>+£1.50</span></li>
          <li><span class="name">Upgrade to 300g</span><span>+£3.50</span></li>
          <li><span class="name">Upgrade to 300g</span><span>+£4.00</span></li>
        </ul>
      </div>
      <div style="width:110px">
        <h3 class="script sub-head">Extras</h3>
        <ul class="plain">
          <li><span class="name">Halloumi</span><span>+£3.50</span></li>
          <li><span class="name">Tzatziki</span><span>+£1.00</span></li>
        </ul>
        <h3 class="script sub-head" style="margin-top:10px">Pita Bread</h3>
        <ul class="plain">
          <li><span class="name">No Pita</span></li>
          <li><span class="name">1 x Pita</span></li>
          <li><span class="name">2 x Pita</span><span>+£1.00</span></li>
        </ul>
      </div>
    </div>
  </section>

  <section class="abs" style="left:438px;top:752px;width:390px">
    <p class="platter-desc">Get a whole meal all wrapped up with our Greek pita wraps. Choose the base (meat skewers, gyros, halloumi or kebab), then add one of our home made sauces. Served with fries and a fresh salad on the side.</p>
    <div style="display:flex;gap:28px;margin-top:14px">
      <div style="width:250px">
        <h3 class="script sub-head">Meat Options <span style="font-size:16px">(2 Skewers)</span></h3>
        <ul class="plain">
          <li><span class="name">Chicken Skewers</span></li>
          <li><span class="name">Pork Skewers</span></li>
          <li><span class="name">Kebab (Lamb &amp; Beef)</span></li>
          <li><span class="name">Mixed Gyros (Chicken &amp; Pork)</span></li>
          <li><span class="name">Upgrade to 3 Skewers</span><span>+£3.00</span></li>
        </ul>
        <h3 class="script sub-head" style="margin-top:10px">Sides</h3>
        <ul class="plain">
          <li><span class="name">Fries</span></li>
          <li><span class="name">Side Salad</span><span>+£1.00</span></li>
        </ul>
      </div>
      <div style="width:110px">
        <h3 class="script sub-head">Extras</h3>
        <ul class="plain">
          <li><span class="name">Halloumi</span><span>+£3.50</span></li>
          <li><span class="name">Tzatziki</span><span>+£1.00</span></li>
        </ul>
        <h3 class="script sub-head" style="margin-top:10px">Pita Bread</h3>
        <ul class="plain">
          <li><span class="name">No Pita</span></li>
          <li><span class="name">1 x Pita</span></li>
          <li><span class="name">2 x Pita</span><span>+£1.00</span></li>
        </ul>
      </div>
    </div>
  </section>

  <div class="abs brand script"><span class="brand-dot"></span><span>Olive Branch<br>Kitchen</span></div>

</main>
</body>
</html>
```